PDN Letterhead

We need a letterhead design that will be able to be used on all marketing products (letterhead, mail chimp, envelops, business cards, etc.) We are a law firm specializing primarily in transportation law but offer a wide range of services to our clients. We would like the design to be modern, simple, and professional. Our colors are black and gold, however, we've incorporated dark gray and white on other marketing products such as our website.

```html
<!DOCTYPE html>
<html lang="en">
<head>
<meta charset="utf-8">
<title>PDN Stationery Set</title>
<link href="https://fonts.googleapis.com/css2?family=Cinzel:wght@500&family=Open+Sans:wght@400;600;700&display=swap" rel="stylesheet">
<style>
  :root {
    --ink: #141414;
    --gold: #bfa17e;
    --paper: #f7f7f5;
    --backdrop: #e9e4dc;
    --text: #2a2a2a;
  }
  * { margin: 0; padding: 0; box-sizing: border-box; }
  html, body { width: 1200px; height: 791px; overflow: hidden; }
  body {
    background: var(--backdrop);
    position: relative;
    font-family: "Open Sans", Arial, sans-serif;
    color: var(--text);
  }
  .sheet {
    position: absolute;
    background: var(--paper);
    box-shadow: 0 4px 10px rgba(0,0,0,.18);
    overflow: hidden;
  }
  .sheet .trim { position: absolute; inset: 0; width: 100%; height: 100%; }
  .brand-name {
    position: absolute;
    font-family: "Cinzel", Georgia, serif;
    font-weight: 500;
    color: var(--ink);
    letter-spacing: .06em;
    line-height: 1;
    white-space: nowrap;
  }
  .contact { position: absolute; font-size: 7.4px; line-height: 1; }
  .contact li { list-style: none; display: flex; align-items: center; gap: 5px; white-space: nowrap; }
  .contact svg { width: 6px; height: 6px; fill: var(--gold); flex: none; }

  /* Letterhead */
  .letterhead { left: 139px; top: 40px; width: 414px; height: 533px; }
  .letterhead .brand-name { left: 0; right: 0; top: 76px; text-align: center; font-size: 30px; }
  .letterhead .contact {
    left: 66px; top: 496px; color: #fff; font-size: 7.6px;
    display: grid; grid-template-columns: auto auto; gap: 5px 8px;
  }

  /* Envelope */
  .envelope { left: 669px; top: 137px; width: 448px; height: 197px; }
  .envelope .brand-name { left: 27px; top: 55px; font-size: 26px; }
  .envelope .contact { left: 28px; top: 102px; }
  .envelope .contact li + li { margin-top: 4.5px; }

  /* Business cards */
  .card { top: 435px; width: 202px; height: 120px; }
  .card-front { left: 664px; }
  .card-front .brand-name { left: 0; right: 0; top: 46px; text-align: center; font-size: 26px; }
  .card-back { left: 909px; }
  .card-back .brand-name { left: 14px; top: 51px; font-size: 20px; }
  .card-back .divider { position: absolute; left: 94px; top: 7px; width: 1.5px; height: 108px; background: var(--ink); }
  .card-back .person { position: absolute; left: 99px; top: 26px; }
  .person-name { font-weight: 700; font-size: 10px; color: var(--ink); line-height: 1; }
  .person-role { font-size: 6.2px; margin-top: 2px; }
  .card-back .contact { left: 99px; top: 51px; font-size: 6.4px; }
  .card-back .contact li + li { margin-top: 4.5px; }
  .card-back .contact svg { width: 5px; height: 5px; }
</style>
</head>
<body>

<svg width="0" height="0" style="position:absolute">
  <defs>
    <symbol id="icon-phone" viewBox="0 0 10 10"><path d="M2 0.5 L3.6 2.6 L2.7 3.6 Q3.8 5.9 6.4 7.3 L7.4 6.4 L9.5 8 L8.4 9.5 Q2.6 8.8 0.5 1.6 Z"/></symbol>
    <symbol id="icon-mail" viewBox="0 0 10 10"><path d="M0 2 H10 V8.5 H0 Z M0.6 2.4 L5 5.6 L9.4 2.4" /></symbol>
    <symbol id="icon-pin" viewBox="0 0 10 10"><path d="M5 0 A3.6 3.6 0 0 1 8.6 3.6 C8.6 6 5 10 5 10 C5 10 1.4 6 1.4 3.6 A3.6 3.6 0 0 1 5 0 Z M5 2.2 A1.4 1.4 0 1 0 5 5 A1.4 1.4 0 1 0 5 2.2 Z" fill-rule="evenodd"/></symbol>
    <symbol id="icon-web" viewBox="0 0 10 10"><circle cx="5" cy="5" r="4.6"/></symbol>
  </defs>
</svg>

<!-- Letterhead -->
<section class="sheet letterhead" aria-label="Letterhead">
  <svg class="trim" viewBox="0 0 414 533" preserveAspectRatio="none">
    <rect x="121" y="0" width="293" height="13" fill="var(--gold)"/>
    <polygon points="0,0 68,0 0,68" fill="var(--ink)"/>
    <polygon points="89,0 121,0 0,121 0,89" fill="var(--ink)"/>
    <polygon points="0,490 360,490 331,519 0,519" fill="var(--ink)"/>
    <polygon points="323,533 341,533 414,460 414,442" fill="var(--gold)"/>
    <polygon points="359,533 379,533 414,498 414,478" fill="var(--gold)"/>
  </svg>
  <div class="brand-name">PDN</div>
  <ul class="contact">
    <li><svg><use href="#icon-phone"/></svg>+111 555 0142</li>
    <li><svg><use href="#icon-mail"/></svg>office@pdnlaw.com</li>
    <li><svg><use href="#icon-pin"/></svg>Ashby Lane, London</li>
    <li><svg><use href="#icon-web"/></svg>www.pdnlaw.com</li>
  </ul>
</section>

<!-- Envelope -->
<section class="sheet envelope" aria-label="Envelope">
  <svg class="trim" viewBox="0 0 448 197" preserveAspectRatio="none">
    <polygon points="0,176 393,176 372,197 0,197" fill="var(--ink)"/>
    <polygon points="374,197 396,197 448,145 448,123" fill="var(--gold)"/>
    <polygon points="411,197 429,197 448,178 448,160" fill="var(--gold)"/>
  </svg>
  <div class="brand-name">PDN</div>
  <ul class="contact">
    <li><svg><use href="#icon-mail"/></svg>office@pdnlaw.com</li>
    <li><svg><use href="#icon-phone"/></svg>+111 555 0142</li>
    <li><svg><use href="#icon-pin"/></svg>Ashby Lane, London</li>
    <li><svg><use href="#icon-web"/></svg>www.pdnlaw.com</li>
  </ul>
</section>

<!-- Business card, front -->
<section class="sheet card card-front" aria-label="Business card front">
  <svg class="trim" viewBox="0 0 202 120" preserveAspectRatio="none">
    <rect x="34" y="0" width="168" height="6" fill="var(--gold)"/>
    <rect x="0" y="114" width="168" height="6" fill="var(--gold)"/>
    <polygon points="0,0 20,0 0,20" fill="var(--ink)"/>
    <polygon points="27,0 38,0 0,38 0,27" fill="var(--ink)"/>
    <polygon points="164,120 175,120 202,93 202,82" fill="var(--ink)"/>
    <polygon points="182,120 202,120 202,100" fill="var(--ink)"/>
  </svg>
  <div class="brand-name">PDN</div>
</section>

<!-- Business card, back -->
<section class="sheet card card-back" aria-label="Business card back">
  <svg class="trim" viewBox="0 0 202 120" preserveAspectRatio="none">
    <rect x="34" y="0" width="168" height="6" fill="var(--gold)"/>
    <rect x="0" y="114" width="168" height="6" fill="var(--gold)"/>
    <polygon points="0,0 20,0 0,20" fill="var(--ink)"/>
    <polygon points="27,0 38,0 0,38 0,27" fill="var(--ink)"/>
    <polygon points="164,120 175,120 202,93 202,82" fill="var(--ink)"/>
    <polygon points="182,120 202,120 202,100" fill="var(--ink)"/>
  </svg>
  <div class="brand-name">PDN</div>
  <div class="divider"></div>
  <div class="person">
    <p class="person-name">Elin Varga</p>
    <p class="person-role">Director</p>
  </div>
  <ul class="contact">
    <li><svg><use href="#icon-mail"/></svg>office@pdnlaw.com</li>
    <li><svg><use href="#icon-phone"/></svg>+111 555 0142</li>
    <li><svg><use href="#icon-pin"/></svg>Ashby Lane, London</li>
    <li><svg><use href="#icon-web"/></svg>www.pdnlaw.com</li>
  </ul>
</section>

</body>
</html>
```